Coralbend Pastoral Traders Business Cards

We require business cards revamped with our logo. A few details we would like to use.

1. Round Edges
2. Our logo over the top of a wagyu cattle background photo on one side of the card

Other side of the card has the below details.

1. Person Name (First & Last)
2. Job Position
3. Mobile Number
4. Email Address
5. Website Address

Simple & Neat.

Target Market(s)

Sales

Industry/Entity Type

Agriculture

Contact Information for Business Card

CORALBEND PASTORAL TRADERS

Colors

Designer to choose colors to be used in the design.

Requirements
Must have
• Company Logo

```html
<!DOCTYPE html>
<html lang="en">
<head>
<meta charset="utf-8">
<title>Coralbend Pastoral Traders – Business Cards</title>
<link rel="stylesheet" href="https://fonts.googleapis.com/css2?family=Poppins:wght@400;500;700&display=swap">
<style>
  :root {
    --stage: #222222;
    --maroon: #7a1216;
    --maroon-deep: #5e0d14;
    --accent-red: #8e1b1b;
    --paper: #ffffff;
    --ink: #1c1c1c;
    --cream: #f1ebe6;
  }
  * { box-sizing: border-box; margin: 0; padding: 0; }
  html, body { width: 1200px; height: 780px; overflow: hidden; }
  body {
    background: var(--stage);
    font-family: "Poppins", sans-serif;
    position: relative;
  }
  .card {
    position: absolute;
    top: 240px;
    width: 520px;
    height: 300px;
    border-radius: 22px;
    overflow: hidden;
  }
  /* Contact side */
  .card--contact { left: 50px; background: var(--paper); }
  .contact-band {
    position: absolute; inset: 0;
    background: var(--maroon);
    clip-path: polygon(0 168px, 450px 300px, 0 300px);
  }
  .edge-tab {
    position: absolute; right: 0; top: 190px;
    width: 10px; height: 44px; background: var(--maroon);
  }
  .brand {
    position: absolute; left: 36px; top: 34px;
    display: flex; align-items: center; gap: 10px;
    color: var(--maroon-deep);
    font-weight: 700; font-size: 17px; letter-spacing: 0.04em;
  }
  .brand-dot {
    width: 26px; height: 26px; border-radius: 50%;
    background: var(--maroon-deep); flex: none;
  }
  .address {
    position: absolute; left: 36px; top: 94px;
    color: var(--accent-red); font-size: 13px; line-height: 1.45;
  }
  .person {
    position: absolute; right: 40px; top: 128px; text-align: right;
  }
  .person-name { color: var(--maroon); font-size: 28px; line-height: 1.1; }
  .person-name .first { font-weight: 700; }
  .person-name .last { font-weight: 400; }
  .person-role { color: var(--ink); font-size: 13px; font-weight: 500; margin-top: 4px; }
  .contact-list {
    position: absolute; left: 26px; top: 224px;
    list-style: none; color: var(--cream); font-size: 12.5px;
  }
  .contact-list li { display: flex; align-items: center; gap: 8px; line-height: 1.75; }
  .contact-list svg { width: 12px; height: 12px; flex: none; }
  /* Brand side */
  .card--brand { left: 630px; background: var(--maroon); display: flex; align-items: center; justify-content: center; }
  .brand--large {
    position: static; color: var(--cream);
    font-size: 22px; gap: 14px; letter-spacing: 0.06em;
  }
  .brand--large .brand-dot { width: 34px; height: 34px; background: var(--cream); }
</style>
</head>
<body>
  <section class="card card--contact">
    <div class="contact-band"></div>
    <div class="edge-tab"></div>
    <div class="brand"><span class="brand-dot"></span>CORALBEND PASTORAL TRADERS</div>
    <p class="address">418 Saltbush Rd. Suite 12<br>Dalby, QLD 4405</p>
    <div class="person">
      <h1 class="person-name"><span class="first">Maren</span> <span class="last">Tolliver</span></h1>
      <p class="person-role">Founder &amp; CEO</p>
    </div>
    <ul class="contact-list">
      <li>
        <svg viewBox="0 0 24 24" fill="currentColor" aria-hidden="true"><path d="M6.6 10.8a15 15 0 0 0 6.6 6.6l2.2-2.2a1 1 0 0 1 1-.25 11.4 11.4 0 0 0 3.6.57 1 1 0 0 1 1 1V20a1 1 0 0 1-1 1A17 17 0 0 1 3 4a1 1 0 0 1 1-1h3.5a1 1 0 0 1 1 1c0 1.250.2 2.45.57 3.57a1 1 0 0 1-.25 1z"/></svg>
        (07) 4662 1938
      </li>
      <li>
        <svg viewBox="0 0 24 24" fill="none" stroke="currentColor" stroke-width="2" aria-hidden="true"><rect x="3" y="5" width="18" height="14" rx="2"/><path d="M3 7l9 6 9-6"/></svg>
        hello@coralbendtraders.com
      </li>
      <li>
        <svg viewBox="0 0 24 24" fill="none" stroke="currentColor" stroke-width="2" aria-hidden="true"><circle cx="12" cy="12" r="9"/><path d="M3 12h18M12 3a14 14 0 0 1 0 18M12 3a14 14 0 0 0 0 18"/></svg>
        www.coralbendtraders.com
      </li>
    </ul>
  </section>

  <section class="card card--brand">
    <div class="brand brand--large"><span class="brand-dot"></span>CORALBEND PASTORAL TRADERS</div>
  </section>
</body>
</html>
```